service truck wrap For KT Fabworks

i want a simple wrap for my work truck,i do mobile welding,Steel fabrication,machining,line boring, industrial maintenance,
I want to cover the entire cube (sides and back) and maybe some info on th truck but not a full wrap

i want to put my logo in the design and my phone numer, with all my offered services
I will add more detail like my logo tomorrow

Target Market(s)

industrial

Industry/Entity Type

welding , machining, industrial maintenance

Requirements
Must have
• business name: KT Fabworks , my Phone number 506-555-0187, my logo

```html
<!DOCTYPE html>
<html lang="en">
<head>
<meta charset="utf-8">
<title>KT Fabworks – Service Truck Wrap</title>
<link rel="stylesheet" href="https://fonts.googleapis.com/css2?family=Abel&family=Rubik:wght@500;700&display=swap">
<style>
  :root {
    --wrap-red: #c81e22;
    --wrap-red-deep: #9e1519;
    --wrap-black: #2b2a2a;
    --wrap-white: #ffffff;
    --bare-panel: #e3e5e8;
    --page-bg: #ffffff;
  }
  html, body {
    margin: 0;
    padding: 0;
    width: 1200px;
    height: 857px;
    overflow: hidden;
    background: var(--page-bg);
  }
  .wrap-sheet {
    position: absolute;
    left: 31px;
    top: 22px;
    width: 1137px;
    height: 812px;
  }
  .fill-red { fill: url(#redSweep); }
  .fill-black { fill: var(--wrap-black); }
  .fill-bare { fill: var(--bare-panel); }
  .rule-dark { stroke: var(--wrap-black); stroke-width: 3; }
  .swoosh-white { fill: none; stroke: var(--wrap-white); }
  .swoosh-black { fill: none; stroke: var(--wrap-black); }
  .mark-ring { fill: none; stroke: var(--wrap-white); stroke-width: 6; }
  .service {
    font-family: "Rubik", sans-serif;
    font-weight: 500;
    fill: var(--wrap-white);
  }
  .service-lg { font-size: 22px; }
  .service-sm { font-size: 14px; }
  .service-rear { font-size: 20px; }
  .brand-name {
    font-family: "Abel", sans-serif;
    fill: var(--wrap-white);
  }
  .phone-pill { fill: var(--wrap-black); }
  .phone {
    font-family: "Rubik", sans-serif;
    font-weight: 500;
    fill: var(--wrap-white);
  }
</style>
</head>
<body>
<svg class="wrap-sheet" viewBox="0 0 2274 1624" xmlns="http://www.w3.org/2000/svg">
  <defs>
    <linearGradient id="redSweep" x1="0" y1="0" x2="1" y2="1">
      <stop offset="0" stop-color="var(--wrap-red-deep)"/>
      <stop offset="0.5" stop-color="var(--wrap-red)"/>
      <stop offset="1" stop-color="var(--wrap-red)"/>
    </linearGradient>
    <clipPath id="cubeSide">
      <path d="M47 167 H610 V263 H487 V543 H47 Z"/>
    </clipPath>
    <clipPath id="cabDoor">
      <path d="M537 393 H900 Q1000 405 1035 470 V518 H537 Z"/>
    </clipPath>
    <clipPath id="cubeBack">
      <rect x="855" y="955" width="520" height="542"/>
    </clipPath>

    <g id="sideArt">
      <g clip-path="url(#cubeSide)">
        <rect class="fill-red" x="47" y="167" width="563" height="376"/>
        <circle class="swoosh-white" cx="60" cy="355" r="255" stroke-width="22"/>
        <circle class="fill-black" cx="60" cy="355" r="245"/>
        <line class="rule-dark" x1="290" y1="263" x2="610" y2="263"/>
        <line class="rule-dark" x1="312" y1="305" x2="487" y2="305"/>
        <line class="rule-dark" x1="316" y1="347" x2="487" y2="347"/>
      </g>
      <rect class="phone-pill" x="310" y="415" width="163" height="38" rx="10"/>
      <circle class="mark-ring" cx="164" cy="296" r="60"/>
      <g clip-path="url(#cabDoor)">
        <path class="fill-red" d="M537 405 H900 Q1000 405 1035 470 V518 H537 Z"/>
        <path class="fill-black" d="M537 393 H718 Q740 470 690 518 H537 Z"/>
        <path class="swoosh-black" d="M825 525 Q860 430 1030 482" stroke-width="28"/>
        <path class="swoosh-white" d="M808 525 Q845 412 1035 462" stroke-width="9"/>
      </g>
      <circle class="mark-ring" cx="607" cy="443" r="30" style="stroke-width:4"/>
    </g>
  </defs>

  <!-- Driver side -->
  <use href="#sideArt"/>
  <g class="side-left-text">
    <text class="service service-lg" x="288" y="217">Welding</text>
    <text class="service service-lg" x="302" y="252">Fabrication</text>
    <text class="service service-lg" x="318" y="292">Machining</text>
    <text class="service service-lg" x="324" y="334">Line boring</text>
    <text class="service service-lg" x="324" y="373">Industrial</text>
    <text class="service service-lg" x="324" y="399">maintenance</text>
    <text class="brand-name" x="164" y="398" font-size="31" text-anchor="middle">KT Fabworks</text>
    <text class="phone" x="391" y="442" font-size="22" text-anchor="middle">506-555-0187</text>
    <text class="service service-sm" x="730" y="440">Welding</text>
    <text class="service service-sm" x="730" y="464">Fabrication</text>
    <text class="service service-sm" x="730" y="488">Machining</text>
    <text class="brand-name" x="607" y="496" font-size="16" text-anchor="middle">KT Fabworks</text>
  </g>

  <!-- Passenger side -->
  <use href="#sideArt" transform="translate(2274 0) scale(-1 1)"/>
  <g class="side-right-text">
    <text class="service service-lg" x="1986" y="217" text-anchor="end">Welding</text>
    <text class="service service-lg" x="1972" y="252" text-anchor="end">Fabrication</text>
    <text class="service service-lg" x="1956" y="292" text-anchor="end">Machining</text>
    <text class="service service-lg" x="1950" y="334" text-anchor="end">Line boring</text>
    <text class="service service-lg" x="1950" y="373" text-anchor="end">Industrial</text>
    <text class="service service-lg" x="1950" y="399" text-anchor="end">maintenance</text>
    <text class="brand-name" x="2110" y="398" font-size="31" text-anchor="middle">KT Fabworks</text>
    <text class="phone" x="1883" y="442" font-size="22" text-anchor="middle">506-555-0187</text>
    <text class="service service-sm" x="1544" y="440" text-anchor="end">Welding</text>
    <text class="service service-sm" x="1544" y="464" text-anchor="end">Fabrication</text>
    <text class="service service-sm" x="1544" y="488" text-anchor="end">Machining</text>
    <text class="brand-name" x="1667" y="496" font-size="16" text-anchor="middle">KT Fabworks</text>
  </g>

  <!-- Rear -->
  <g class="rear-panel" clip-path="url(#cubeBack)">
    <rect class="fill-bare" x="855" y="955" width="520" height="542"/>
    <circle class="swoosh-white" cx="880" cy="1340" r="230" stroke-width="20"/>
    <circle class="fill-black" cx="880" cy="1340" r="220"/>
    <circle class="swoosh-white" cx="1400" cy="1530" r="300" stroke-width="20"/>
    <circle class="fill-red" cx="1400" cy="1530" r="290"/>
  </g>
  <circle class="mark-ring" cx="957" cy="1305" r="55"/>
  <g class="rear-text">
    <text class="brand-name" x="957" y="1398" font-size="29" text-anchor="middle">KT Fabworks</text>
    <text class="service service-rear" x="1352" y="1302" text-anchor="end">Welding</text>
    <text class="service service-rear" x="1352" y="1327" text-anchor="end">Fabrication</text>
    <text class="service service-rear" x="1352" y="1352" text-anchor="end">Machining</text>
    <text class="service service-rear" x="1352" y="1377" text-anchor="end">Line boring</text>
    <text class="service service-rear" x="1352" y="1402" text-anchor="end">Industrial</text>
    <text class="service service-rear" x="1352" y="1424" text-anchor="end">maintenance</text>
    <rect class="phone-pill" x="1128" y="1434" width="224" height="48" rx="14"/>
    <text class="phone" x="1240" y="1469" font-size="30" text-anchor="middle">506-555-0187</text>
  </g>
</svg>
</body>
</html>
```